World leading Water filters German made

I am a local Plumbing business who is authorised water filter installer
I want to do a Flyer design double sided targeting niche market for Water Filters.
My company colours are black background with white writing.
( but happy to go into different colours to capture more people )
I want all my stuff, sleek and professional with the same fonts throughout.
Www.brightvalepipeworks.au
Is my website you can see how I do things there.
I want the local business awards finalist logo on the flyer too ( it’ll be in the photo)
This Flyer I want all about health and wellness making big points on water filtration benefits
Massive to included HYDROGEN WATER AND ALKALINE WATER ,
REMOVE FLUORIDE
I don’t know whether to have it with the pre-save branded information I sent over, but I don’t want the company other companies name everywhere
I want the main focus about my company Brightvale Pipeworks And Boiler Experts
I want the focus to be about a family owned and run Illawarra local business establish for over 20 years.
Please note I have included a Customer brochure the company has designed so you can see some key points on the second page about the products. I want this a lot more eye-catching and appealing please
Target Market(s)
Health and wellness people
Colors
Designer to choose colors to be used in the design.
Requirements
Must have
- Call Trevor 0438 627 195, my website , social media buttons ,
Nice to have
- World leading , health and wellness ,
Should not have
- Any information to lead them away from calling myself , I’m the authorities dealer for purestream supply but I want to no have as much anout them.

```html
<!DOCTYPE html>
<html lang="en">
<head>
<meta charset="utf-8">
<title>Brightvale Pipeworks – Water Filtration Flyer</title>
<link href="https://fonts.googleapis.com/css2?family=Open+Sans:wght@300;400;600;700;800&display=swap" rel="stylesheet">
<style>
:root{
  --stage:#93c4c3;
  --charcoal:#333334;
  --brand-blue:#2a8fd6;
  --sky:#3ea3e6;
  --paper:#f4f4f4;
  --ink:#2b2b2b;
  --muted:#6b6b6b;
  --soft:#d8d8d8;
  --photo-steel:#8d9399;
  --photo-warm:#b9aa95;
}
*{box-sizing:border-box;margin:0;padding:0}
html,body{width:1200px;height:900px;overflow:hidden;background:var(--stage);font-family:"Open Sans",Arial,sans-serif}
.flyer{position:absolute;top:54px;width:560px;height:792px;background:var(--paper);overflow:hidden;box-shadow:0 10px 30px rgba(0,0,0,.18)}
.flyer--front{left:26px}
.flyer--back{left:614px}
.flyer__art{position:absolute;inset:0}

/* brand name block */
.brand-mark{position:absolute;display:flex;align-items:center;gap:10px;color:#fff;font-weight:700;line-height:1.15;letter-spacing:.5px;text-transform:uppercase}
.brand-mark__square{width:14px;height:14px;border:2px solid #fff;flex:none}
.brand-mark--header{left:40px;top:120px;font-size:15px}
.brand-mark--footer{right:28px;top:736px;font-size:12px}

/* front */
.hero-headline{position:absolute;left:40px;top:200px;font-size:33px;line-height:1.08;text-transform:uppercase}
.hero-headline__plain{color:#fff;font-weight:300;display:block}
.hero-headline__accent{color:var(--sky);font-weight:700;display:block}
.health-title{position:absolute;left:40px;top:488px;width:480px;text-transform:uppercase;color:var(--ink);font-size:23px;line-height:1.2}
.health-title b{font-weight:800}
.health-title span{font-weight:300}
.intro-copy{position:absolute;left:40px;top:556px;width:480px;font-size:10.5px;line-height:1.5;color:var(--muted)}
.intro-copy strong{color:var(--ink);font-weight:700}
.why-title{position:absolute;left:40px;top:616px;color:var(--brand-blue);font-weight:700;font-size:20px;text-transform:uppercase}
.benefits{position:absolute;left:30px;top:658px;width:500px;display:flex;justify-content:space-between;list-style:none}
.benefit{width:92px;text-align:center;font-size:10.5px;font-weight:700;color:var(--ink);line-height:1.25}
.benefit__icon{width:46px;height:46px;border-radius:50%;background:var(--charcoal);margin:0 auto 8px;display:flex;align-items:center;justify-content:center}

/* back */
.services-title{position:absolute;left:0;right:0;top:30px;text-align:center;font-weight:700;font-size:24px;color:var(--ink);letter-spacing:1px}
.services-grid{position:absolute;left:34px;top:78px;width:492px;display:grid;grid-template-columns:repeat(3,1fr);column-gap:22px;row-gap:14px;list-style:none}
.service{text-align:center}
.service__photo{height:92px;border:3px solid #fff;box-shadow:0 0 0 1px #bbb}
.service__name{margin-top:7px;color:var(--brand-blue);font-weight:700;font-size:10.5px;text-transform:uppercase}
.service__text{margin-top:3px;font-size:8.5px;line-height:1.35;color:var(--muted)}
.service--on-dark .service__text{color:var(--soft)}
.book{position:absolute;left:0;right:0;top:566px;text-align:center}
.book__title{color:var(--sky);font-weight:700;font-size:22px;text-transform:uppercase}
.book__lead{color:var(--soft);font-size:10.5px;margin-top:2px}
.book__phone{color:var(--sky);font-weight:700;font-size:36px;line-height:1.2;margin-top:2px;letter-spacing:1px}
.book__phone span{color:#fff;font-weight:300;font-size:22px;letter-spacing:0}
.book__tag{color:#fff;font-weight:700;font-size:14px}
.book__web{color:var(--soft);font-size:12px;margin-top:1px}
.social{position:absolute;left:0;right:0;top:736px;display:flex;justify-content:center;gap:10px;list-style:none}
.social__button{width:24px;height:24px;border-radius:50%;background:var(--sky)}
.award-badge{position:absolute;left:30px;top:712px;width:60px;height:60px;border-radius:50%;background:radial-gradient(circle at 40% 35%,#e8d9a6,#b99a4b);border:4px solid #c0272d}
</style>
</head>
<body>

<section class="flyer flyer--front" aria-label="Flyer front">
  <svg class="flyer__art" width="560" height="792" viewBox="0 0 560 792">
    <defs>
      <clipPath id="photoClip"><path d="M205 0H560V280C520 288 475 268 445 240C405 205 335 228 285 218C230 205 210 145 205 80Z"/></clipPath>
      <linearGradient id="plantGrad" x1="0" y1="0" x2="1" y2="1"><stop offset="0" stop-color="#8d9399"/><stop offset="1" stop-color="#b9aa95"/></linearGradient>
      <linearGradient id="pipeGrad" x1="0" y1="0" x2="1" y2="1"><stop offset="0" stop-color="#f2f2f2"/><stop offset=".6" stop-color="#c9c9c9"/><stop offset="1" stop-color="#8fb8df"/></linearGradient>
    </defs>
    <path d="M0 0H560V400C470 400 420 440 330 440C230 440 140 470 0 470Z" fill="#333334"/>
    <path d="M190 0H560V290C520 300 470 280 440 250C400 215 330 240 280 230C220 215 200 150 190 80Z" fill="#3ea3e6"/>
    <rect x="200" y="0" width="360" height="282" fill="url(#plantGrad)" clip-path="url(#photoClip)" role="img" aria-label="Photo of a stainless steel German made water filtration unit with pressure gauges"/>
    <path d="M0 470C140 470 230 440 330 440C420 440 470 400 560 400V792H0Z" fill="#e2e2e2"/>
    <path d="M0 500C160 490 260 470 380 468C470 468 520 450 560 440V792H0Z" fill="#f4f4f4"/>
    <rect x="300" y="240" width="240" height="210" rx="40" fill="url(#pipeGrad)" role="img" aria-label="Illustration of white and blue water filter pipe fittings"/>
  </svg>

  <div class="brand-mark brand-mark--header"><span class="brand-mark__square"></span><span>Brightvale Pipeworks<br>&amp; Boiler Experts</span></div>

  <h1 class="hero-headline">
    <span class="hero-headline__plain">Need</span>
    <span class="hero-headline__accent">a plumber</span>
    <span class="hero-headline__accent">or hot water</span>
    <span class="hero-headline__accent">specialist</span>
    <span class="hero-headline__plain">now?</span>
  </h1>

  <h2 class="health-title"><span>Hydrogen</span> <b>water and</b><br><b>alkaline water</b><span>, remove fluoride</span></h2>
  <p class="intro-copy"><strong>Family owned and run Illawarra business, established for over 20 years.</strong> We supply and install world leading German made water filters for cleaner, healthier drinking water at home – throughout Wollongong, Shellharbour &amp; Shoalhaven. Call Trevor on 0438 627 195.</p>

  <h3 class="why-title">Why choose us?</h3>
  <ul class="benefits">
    <li class="benefit"><div class="benefit__icon"><svg width="26" height="26" viewBox="0 0 26 26" fill="none" stroke="#fff" stroke-width="2"><circle cx="13" cy="13" r="10"/><path d="M13 7v6l4 3"/></svg></div>Available 24/7</li>
    <li class="benefit"><div class="benefit__icon"><svg width="26" height="26" viewBox="0 0 26 26" fill="none" stroke="#fff" stroke-width="2"><rect x="5" y="4" width="16" height="18" rx="2"/><path d="M9 10h8M9 14h8M9 18h5"/></svg></div>Fully licensed &amp; insured</li>
    <li class="benefit"><div class="benefit__icon"><svg width="26" height="26" viewBox="0 0 26 26" fill="none" stroke="#fff" stroke-width="2"><circle cx="13" cy="9" r="4"/><path d="M5 22c0-5 4-8 8-8s8 3 8 8"/></svg></div>Family run local business</li>
    <li class="benefit"><div class="benefit__icon"><svg width="26" height="26" viewBox="0 0 26 26" fill="none" stroke="#fff" stroke-width="2"><path d="M13 3l8 3v6c0 5-4 9-8 11-4-2-8-6-8-11V6z"/><path d="M9 13l3 3 5-6"/></svg></div>Lifetime labour warranty</li>
    <li class="benefit"><div class="benefit__icon"><svg width="26" height="26" viewBox="0 0 26 26" fill="none" stroke="#fff" stroke-width="2"><rect x="4" y="7" width="18" height="12" rx="2"/><path d="M13 10v6M11 11.5h3.5a1.2 1.2 0 0 1 0 2.4h-3a1.2 1.2 0 0 0 0 2.4H15"/></svg></div>Fixed upfront pricing</li>
  </ul>
</section>

<section class="flyer flyer--back" aria-label="Flyer back">
  <svg class="flyer__art" width="560" height="792" viewBox="0 0 560 792">
    <rect x="0" y="330" width="560" height="462" fill="#333334"/>
  </svg>

  <h2 class="services-title">OUR SERVICES</h2>
  <ul class="services-grid">
    <li class="service"><div class="service__photo" role="img" aria-label="Photo of a plumbing maintenance job" style="background:linear-gradient(135deg,#cfcfcf,#8f8f8f)"></div><p class="service__name">Plumbing maintenance</p><p class="service__text">As plumbing specialists, we guarantee expert installations and swift repairs.</p></li>
    <li class="service"><div class="service__photo" role="img" aria-label="Photo of hot water system units" style="background:linear-gradient(135deg,#d9d4cc,#7d756c)"></div><p class="service__name">Hot water systems</p><p class="service__text">Trust the hot water specialists for all your installations.</p></li>
    <li class="service"><div class="service__photo" role="img" aria-label="Photo of a hot water heater being serviced" style="background:linear-gradient(135deg,#b7312f,#6c5c55)"></div><p class="service__name">Hot water servicing</p><p class="service__text">Trust our skilled plumbers for prompt and reliable hot water services.</p></li>
    <li class="service service--on-dark"><div class="service__photo" role="img" aria-label="Photo of a drain inspection camera screen" style="background:linear-gradient(135deg,#4a4a4a,#1f1f1f)"></div><p class="service__name">Blocked drains</p><p class="service__text">As plumbing specialists, we guarantee expert and swift results.</p></li>
    <li class="service service--on-dark"><div class="service__photo" role="img" aria-label="Photo of a thermal leak detection camera" style="background:linear-gradient(135deg,#e0663a,#2d2d2d)"></div><p class="service__name">Leak detection</p><p class="service__text">Let us help find and fix leaks throughout your plumbing.</p></li>
    <li class="service service--on-dark"><div class="service__photo" role="img" aria-label="Photo of an under-sink water filter installation" style="background:linear-gradient(135deg,#9a8f7f,#4d4740)"></div><p class="service__name">Water filters</p><p class="service__text">Hydrogen &amp; alkaline water, fluoride removed – supplied and installed.</p></li>
    <li class="service service--on-dark"><div class="service__photo" role="img" aria-label="Photo of a gas leak detector in use" style="background:linear-gradient(135deg,#d8dde2,#7b8590)"></div><p class="service__name">Gas plumbers</p><p class="service__text">With many years of experience you can trust us with your gas plumbing.</p></li>
    <li class="service service--on-dark"><div class="service__photo" role="img" aria-label="Photo of an emergency pipe repair in the ground" style="background:linear-gradient(135deg,#9a8a6e,#4e4536)"></div><p class="service__name">Emergency plumber</p><p class="service__text">With our 24/7 call-out service we are your go-to for emergencies.</p></li>
    <li class="service service--on-dark"><div class="service__photo" role="img" aria-label="Photo of a bathroom toilet and tap" style="background:linear-gradient(135deg,#c9c3ba,#6f6a63)"></div><p class="service__name">Toilet repairs &amp; tap servicing</p><p class="service__text">Enjoy improved functionality and efficiency with expert solutions.</p></li>
  </ul>

  <div class="book">
    <p class="book__title">Book your service</p>
    <p class="book__lead">Family owned Illawarra business for over 20 years – talk to us about healthier water</p>
    <p class="book__phone"><span>Call Trevor</span> 0438 627 195</p>
    <p class="book__tag">24/7 Emergency Plumbing</p>
    <p class="book__web">www.brightvalepipeworks.au</p>
  </div>

  <ul class="social" aria-label="Social media">
    <li class="social__button" aria-label="Social media link"></li>
    <li class="social__button" aria-label="Social media link"></li>
    <li class="social__button" aria-label="Social media link"></li>
  </ul>

  <div class="award-badge" role="img" aria-label="Local business awards finalist badge"></div>
  <div class="brand-mark brand-mark--footer"><span class="brand-mark__square"></span><span>Brightvale Pipeworks<br>&amp; Boiler Experts</span></div>
</section>

</body>
</html>
```